Design Creative Banner or Gif Ads. 3 Designs To Be Selected

Come up with some creative banner ads for stonewell.co.nz

*At least 3 different winning banners will be chosen*

Please provide banner ads / gif ads in common google ads / website banner formats.

They can be gif or static but must stand out while still maintaining clear clean text and visuals, with a premium professional feel (please avoid clip art or anything that gives a cheap message).

Please keep in mind that these will likely be small ads so text needs to be large and if there's there a lot of text then use multiple frames/ pages as submit as a gif.

Style
Minimal & clean lines
Architectural or realistic images
Avoid cartoon styles, clipart, or anything that looks cheap

Font
Nexa or Montserrat or similar

Tone
Premium, serious, trustworthy — fits new builds

Colours
Option 1: Deep Navy (trust & quality) & lighter blues and warm grey
Option 2: Open to bright colours to help the ads stand out, such as (but not limited to) bright pink with black, yellow, fluorescent green, provided the messaging is still done professionally.
Our logo is attached (Stone Well Logo)

Display Sizes
Ad specs for file sizes should be file formats like JPEG, GIF, and PNG, with animations limited to a max of 30 seconds or less.
We will need several different ad sizes provided for each of the 3 selected winning designs.

• Medium Rectangle: 300 × 250 pixels
• Leaderboard: 728 × 90 pixels
• Desktop Banner ad image: (640x360 pixels)
• Desktop Banner ad image 2: (300x600 pixels)
• Possibly one or two other sizes

Flexibility to be creative
The ad text, words, upper/lower case, layout, colour, theme, and images can be adjusted to how you think it will look best. The follow example ads are just examples of what we are after but we are keen to see what you can create.

Recommendations at this point:
1. Avoid text heavy
2. Looking for more Gif ads
3. Imaging: if possible use real stock photo's rather than AI

Themes:

1
Building Soon? Start Here
Free Build Planning Pack:
✓ Build Cost Calculator
✓ Hidden Cost Checklist
✓ Builder Comparison Guide
Build With Confidence
Download Free

2
Before You Choose A Builder
Compare Price, Scope, Risk & Value
Avoid Costly Mistakes
Choose The Right Builder With Confidence
Download The Free Guide

3
Planning A New Build?
Avoid These Common Mistakes:
✗ Hidden Exclusions
✗ Missing Scope
✗ Unrealistic Allowances
✗ Budget Blowouts
Download The Free Guide

4
Before You Buy Land
Know what it could cost to build.
Avoid Costly Building Mistakes
Download Our Free Guides

5
Know Your Build Budget?
• Free Build Cost Calculator
• Hidden Cost Checklist
• Build Planning Tools
Calculate Costs (Download)

Target Market(s)

Landowners looking to build

Industry/Entity Type

Building

Font styles to use
Other font styles liked:
• Nexa or Montserrat or similar

Requirements
Should not have
• Avoid cartoon styles, clipart, or anything that looks cheap

```html
<!DOCTYPE html>
<html lang="en">
<head>
<meta charset="utf-8">
<title>Concept 3: Build Planning Pack – Stonewell banner set</title>
<link href="https://fonts.googleapis.com/css2?family=Montserrat:wght@500;600;700;800;900&display=swap" rel="stylesheet">
<style>
:root{
  --navy:#0b1a33;
  --navy-soft:#1c2c4b;
  --blue:#0b3a9c;
  --btn:#0a3a9e;
  --panel:#f1f2f4;
  --paper:#f8f9fa;
  --paper-shade:#e2e5e9;
  --edge:#d9dce1;
  --label:#6e9a3a;
  --text:#15203a;
  --white:#ffffff;
}
*{box-sizing:border-box;margin:0;padding:0}
html,body{width:800px;height:1200px;overflow:hidden;background:var(--white)}
body{position:relative;font-family:"Montserrat",sans-serif;color:var(--text)}
.abs{position:absolute}
.sheet-header{left:4px;top:4px;width:792px;height:76px;background:var(--navy);color:var(--white);text-align:center}
.sheet-header h1{font-size:26px;font-weight:800;letter-spacing:.5px;margin-top:12px}
.sheet-header p{font-size:15px;font-weight:600;letter-spacing:.6px;margin-top:4px}
.panel{background:var(--panel);border:1px solid var(--edge);overflow:hidden}
.plans{background:linear-gradient(150deg,var(--paper) 0%,#eceef1 55%,var(--paper-shade) 100%)}
.book{position:absolute;background:linear-gradient(155deg,var(--navy-soft) 0%,var(--navy) 60%,#08142a 100%);border-radius:2px 4px 4px 2px;box-shadow:4px 6px 12px rgba(11,26,51,.28);transform:rotate(-5deg)}
.headline{font-weight:900;color:var(--navy);line-height:.98;letter-spacing:-.5px}
.sub{font-weight:800;color:var(--blue);line-height:1.12}
.checks{list-style:none;font-weight:500;color:var(--text);text-transform:uppercase}
.checks li{display:flex;align-items:flex-start;gap:.55em}
.checks svg{flex:none;width:1.15em;height:1.15em;margin-top:.05em}
.btn{background:var(--btn);color:var(--white);font-weight:700;text-align:center;display:flex;align-items:center;justify-content:center;line-height:1.15;text-transform:uppercase;border-radius:2px}
.url{font-weight:700;color:var(--navy);letter-spacing:.3px;text-transform:uppercase}
.size-label{font-size:12px;font-weight:700;color:var(--label)}
.feature{text-align:center;font-size:8.5px;font-weight:600;text-transform:uppercase;line-height:1.25;color:var(--text)}
.feature svg{display:block;margin:0 auto 8px;width:22px;height:22px}
</style>
</head>
<body>
<svg width="0" height="0" style="position:absolute">
  <symbol id="tick" viewBox="0 0 20 20">
    <circle cx="10" cy="10" r="10" fill="#0b1a33"/>
    <path d="M5.5 10.3l3 3 6-6.3" fill="none" stroke="#fff" stroke-width="2.4" stroke-linecap="round" stroke-linejoin="round"/>
  </symbol>
</svg>

<header class="abs sheet-header">
  <h1>CONCEPT 3: BUILD PLANNING PACK</h1>
  <p>EVERYTHING YOU NEED BEFORE YOU BUILD</p>
</header>

<!-- Hero -->
<section class="abs" style="left:4px;top:82px;width:792px;height:443px;background:var(--panel)">
  <div class="abs plans" style="left:0;top:0;width:369px;height:443px">
    <div class="book" role="img" aria-label="Navy hardcover Build Planning Pack book with a house photo on its cover, lying on architectural plans" style="left:42px;top:48px;width:285px;height:360px"></div>
  </div>
  <h2 class="abs headline" style="left:430px;top:28px;font-size:61px">BOUGHT<br>LAND?</h2>
  <p class="abs sub" style="left:430px;top:150px;font-size:31px">AVOID COSTLY<br>BUILD MISTAKES</p>
  <ul class="abs checks" style="left:430px;top:238px;font-size:18.5px">
    <li style="margin-bottom:14px"><svg><use href="#tick"/></svg>Build cost calculator</li>
    <li style="margin-bottom:14px"><svg><use href="#tick"/></svg>Build journey roadmap</li>
    <li><svg><use href="#tick"/></svg>Hidden cost checklist</li>
  </ul>
  <div class="abs btn" style="left:430px;top:348px;width:243px;height:58px;font-size:19px">Download free<br>planning pack</div>
  <p class="abs url" style="left:470px;top:418px;font-size:15px">stonewell.co.nz</p>
</section>

<!-- 728x90 -->
<span class="abs size-label" style="left:22px;top:532px">728x90</span>
<section class="abs panel" style="left:22px;top:551px;width:754px;height:67px">
  <div class="abs plans" style="left:0;top:0;width:83px;height:65px">
    <div class="book" role="img" aria-label="Build Planning Pack book on plans" style="left:16px;top:4px;width:56px;height:58px"></div>
  </div>
  <h2 class="abs headline" style="left:102px;top:10px;font-size:28px">BOUGHT LAND?</h2>
  <p class="abs sub" style="left:103px;top:43px;font-size:12.5px">AVOID COSTLY BUILD MISTAKES</p>
  <ul class="abs checks" style="left:354px;top:9px;font-size:9.5px;line-height:1.15">
    <li style="margin-bottom:6px"><svg><use href="#tick"/></svg>Build cost<br>calculator</li>
    <li><svg><use href="#tick"/></svg>Hidden cost<br>checklist</li>
  </ul>
  <div class="abs btn" style="left:497px;top:13px;width:109px;height:38px;font-size:12.5px">Download<br>free pack</div>
  <p class="abs url" style="left:629px;top:27px;font-size:8.5px">stonewell.co.nz</p>
</section>

<!-- 300x250 -->
<span class="abs size-label" style="left:22px;top:625px">300x250</span>
<section class="abs panel" style="left:22px;top:645px;width:307px;height:193px">
  <div class="abs plans" style="left:150px;top:0;width:155px;height:191px">
    <div class="book" role="img" aria-label="Build Planning Pack book on architectural plans" style="left:18px;top:18px;width:118px;height:160px"></div>
  </div>
  <h2 class="abs headline" style="left:13px;top:12px;font-size:26px">BOUGHT<br>LAND?</h2>
  <p class="abs sub" style="left:13px;top:70px;font-size:15px">AVOID COSTLY<br>BUILD MISTAKES</p>
  <div class="abs btn" style="left:13px;top:120px;width:105px;height:35px;font-size:11.5px">Download<br>free pack</div>
  <p class="abs url" style="left:13px;top:170px;font-size:9px">stonewell.co.nz</p>
</section>

<!-- 336x280 -->
<span class="abs size-label" style="left:352px;top:625px">336x280</span>
<section class="abs panel" style="left:357px;top:645px;width:420px;height:195px">
  <div class="abs plans" style="left:236px;top:0;width:182px;height:193px">
    <div class="book" role="img" aria-label="Build Planning Pack book on architectural plans" style="left:36px;top:12px;width:120px;height:172px"></div>
  </div>
  <h2 class="abs headline" style="left:17px;top:15px;font-size:28px">BOUGHT LAND?</h2>
  <p class="abs sub" style="left:18px;top:51px;font-size:13px">AVOID COSTLY BUILD MISTAKES</p>
  <ul class="abs checks" style="left:18px;top:84px;font-size:10.5px">
    <li style="margin-bottom:7px"><svg><use href="#tick"/></svg>Build cost calculator</li>
    <li style="margin-bottom:7px"><svg><use href="#tick"/></svg>Build journey roadmap</li>
    <li><svg><use href="#tick"/></svg>Hidden cost checklist</li>
  </ul>
  <div class="abs btn" style="left:18px;top:148px;width:150px;height:23px;font-size:10.5px">Download free pack</div>
  <p class="abs url" style="left:18px;top:179px;font-size:9.5px">stonewell.co.nz</p>
</section>

<!-- 300x600 -->
<span class="abs size-label" style="left:22px;top:845px">300x600</span>
<section class="abs panel" style="left:22px;top:862px;width:137px;height:332px">
  <h2 class="abs headline" style="left:12px;top:10px;font-size:20px">BOUGHT<br>LAND?</h2>
  <p class="abs sub" style="left:12px;top:55px;font-size:11px">AVOID COSTLY<br>BUILD MISTAKES</p>
  <ul class="abs checks" style="left:12px;top:92px;font-size:8.5px;line-height:1.25">
    <li style="margin-bottom:7px"><svg><use href="#tick"/></svg>Build cost<br>calculator</li>
    <li style="margin-bottom:7px"><svg><use href="#tick"/></svg>Build journey<br>roadmap</li>
    <li><svg><use href="#tick"/></svg>Hidden cost<br>checklist</li>
  </ul>
  <div class="abs plans" style="left:0;top:168px;width:135px;height:104px">
    <div class="book" role="img" aria-label="Build Planning Pack book on plans" style="left:32px;top:10px;width:78px;height:86px"></div>
  </div>
  <div class="abs btn" style="left:12px;top:284px;width:93px;height:30px;font-size:9px">Download<br>free pack</div>
  <p class="abs url" style="left:12px;top:319px;font-size:7.5px">stonewell.co.nz</p>
</section>

<!-- 336x280 second -->
<span class="abs size-label" style="left:190px;top:845px">336x280</span>
<section class="abs panel" style="left:190px;top:864px;width:335px;height:154px">
  <div class="abs plans" style="left:215px;top:0;width:118px;height:152px">
    <div class="book" role="img" aria-label="Build Planning Pack book on architectural plans" style="left:14px;top:14px;width:94px;height:122px"></div>
  </div>
  <h2 class="abs headline" style="left:15px;top:13px;font-size:24px">BOUGHT LAND?</h2>
  <p class="abs sub" style="left:16px;top:43px;font-size:11px">AVOID COSTLY BUILD MISTAKES</p>
  <ul class="abs checks" style="left:16px;top:67px;font-size:9px">
    <li style="margin-bottom:5px"><svg><use href="#tick"/></svg>Build cost calculator</li>
    <li style="margin-bottom:5px"><svg><use href="#tick"/></svg>Build journey roadmap</li>
    <li><svg><use href="#tick"/></svg>Hidden cost checklist</li>
  </ul>
  <div class="abs btn" style="left:16px;top:120px;width:120px;height:18px;font-size:8.5px">Download free pack</div>
  <p class="abs url" style="left:16px;top:142px;font-size:7px">stonewell.co.nz</p>
</section>

<!-- 640x360 -->
<span class="abs size-label" style="left:185px;top:1021px">640x360</span>
<section class="abs panel" style="left:185px;top:1034px;width:442px;height:160px">
  <div class="abs plans" style="left:283px;top:0;width:157px;height:158px">
    <div class="book" role="img" aria-label="Build Planning Pack book on plans beside a plant" style="left:16px;top:12px;width:128px;height:138px"></div>
  </div>
  <h2 class="abs headline" style="left:16px;top:16px;font-size:26px">BOUGHT LAND?</h2>
  <p class="abs sub" style="left:17px;top:50px;font-size:12px">AVOID COSTLY BUILD MISTAKES</p>
  <div class="abs feature" style="left:12px;top:72px;width:66px">
    <svg viewBox="0 0 24 24" fill="none" stroke="#15203a" stroke-width="1.5"><rect x="5" y="2" width="14" height="20" rx="1.5"/><rect x="8" y="5" width="8" height="4"/><path d="M8 13h1M12 13h1M15.5 13h.5M8 16h1M12 16h1M15.5 16h.5M8 19h1M12 19h1"/></svg>
    Build cost<br>calculator
  </div>
  <div class="abs feature" style="left:92px;top:72px;width:80px;border-left:1px solid var(--edge);border-right:1px solid var(--edge)">
    <svg viewBox="0 0 24 24" fill="none" stroke="#15203a" stroke-width="1.5"><path d="M18 8c0 4-4 8-4 8s-4-4-4-8a4 4 0 018 0z"/><circle cx="14" cy="8" r="1.4"/><path d="M4 21c2-3 6-2 8-4"/><circle cx="4" cy="21" r="1.3"/></svg>
    Build journey<br>roadmap
  </div>
  <div class="abs feature" style="left:183px;top:72px;width:74px">
    <svg viewBox="0 0 24 24" fill="none" stroke="#15203a" stroke-width="1.5"><path d="M18 8c0 4-4 8-4 8s-4-4-4-8a4 4 0 018 0z"/><circle cx="14" cy="8" r="1.4"/><path d="M4 21c2-3 6-2 8-4"/><circle cx="4" cy="21" r="1.3"/></svg>
    Hidden cost<br>checklist
  </div>
  <div class="abs btn" style="left:15px;top:130px;width:131px;height:20px;font-size:9px">Download free pack</div>
  <p class="abs url" style="left:159px;top:135px;font-size:8.5px">stonewell.co.nz</p>
</section>

<!-- 160x600 -->
<span class="abs size-label" style="left:670px;top:846px">160x600</span>
<section class="abs panel" style="left:670px;top:863px;width:107px;height:331px">
  <h2 class="abs headline" style="left:11px;top:12px;font-size:19px">BOUGHT<br>LAND?</h2>
  <p class="abs sub" style="left:11px;top:56px;font-size:10.5px">AVOID<br>COSTLY<br>BUILD<br>MISTAKES</p>
  <ul class="abs checks" style="left:11px;top:118px;font-size:7.8px;line-height:1.3">
    <li style="margin-bottom:8px"><svg><use href="#tick"/></svg>Build cost<br>calculator</li>
    <li style="margin-bottom:8px"><svg><use href="#tick"/></svg>Build journey<br>roadmap</li>
    <li><svg><use href="#tick"/></svg>Hidden cost<br>checklist</li>
  </ul>
  <div class="abs plans" style="left:0;top:203px;width:105px;height:79px">
    <div class="book" role="img" aria-label="Build Planning Pack book" style="left:22px;top:8px;width:66px;height:64px"></div>
  </div>
  <div class="abs btn" style="left:11px;top:290px;width:83px;height:24px;font-size:7.5px">Download<br>free pack</div>
  <p class="abs url" style="left:11px;top:320px;font-size:6.5px">stonewell.co.nz</p>
</section>
</body>
</html>
```